Bref créative
TORV stationery
Stationery
Simple
Marco Daniel Fervone Lusse de Telvin
Administrador
Rua das Acácias nº17 Luanda-Angola
marco.telvin@torv-exemplo.com
www.torv-exemplo.com

```html
<!DOCTYPE html>
<html lang="pt">
<head>
<meta charset="utf-8">
<title>TORV stationery</title>
<link rel="stylesheet" href="https://fonts.googleapis.com/css2?family=Montserrat:wght@700&family=Open+Sans:wght@400;600&display=swap">
<style>
  :root {
    --backdrop: #a27c2f;
    --paper: #ffffff;
    --orange: #f07a1b;
    --orange-light: #f7a43a;
    --blue: #1b64ae;
    --blue-dark: #144c86;
    --grey-flap: #c9cbcf;
    --ink: #333a44;
    --rule: #9aa0a8;
    --ghost: rgba(27, 100, 174, 0.13);
  }
  * { box-sizing: border-box; margin: 0; padding: 0; }
  html, body { width: 1200px; height: 540px; overflow: hidden; }
  body {
    background: var(--backdrop);
    font-family: "Open Sans", Arial, sans-serif;
    color: var(--ink);
    position: relative;
  }
  .sheet, .envelope, .card {
    position: absolute;
    background: var(--paper);
    box-shadow: 0 2px 6px rgba(0,0,0,0.25);
    overflow: hidden;
  }
  .wordmark {
    font-family: "Montserrat", Arial, sans-serif;
    font-weight: 700;
    color: var(--blue);
    letter-spacing: 1px;
    display: flex;
    align-items: center;
    gap: 5px;
    white-space: nowrap;
  }
  .wordmark .mark-square { background: var(--orange); display: block; flex: none; }

  /* Letter & fax sheets */
  .sheet { top: 43px; width: 350px; height: 466px; }
  .sheet--letter { left: 34px; }
  .sheet--fax { left: 404px; }
  .sheet--letter .wordmark { position: absolute; top: 22px; left: 0; right: 0; justify-content: center; font-size: 16px; }
  .sheet--letter .mark-square { width: 14px; height: 14px; }
  .ghost-mark {
    position: absolute;
    font-family: "Montserrat", Arial, sans-serif;
    font-weight: 700;
    color: var(--ghost);
    display: flex; flex-direction: column; align-items: center; gap: 8px;
  }
  .ghost-mark .ghost-square { background: var(--ghost); display: block; }
  .sheet--letter .ghost-mark { left: 18px; top: 150px; font-size: 62px; }
  .sheet--letter .ghost-square { width: 110px; height: 110px; }
  .sheet--fax .ghost-mark { right: 28px; bottom: 50px; font-size: 26px; }
  .sheet--fax .ghost-square { width: 50px; height: 50px; }

  .sheet-footer {
    position: absolute; left: 0; right: 0; bottom: 0;
  }
  .sheet-footer .address {
    padding: 0 16px 5px;
    font-size: 5.5px; line-height: 1.5;
    display: flex; justify-content: space-between;
  }
  .footer-band { height: 18px; display: flex; }
  .footer-band .warm { flex: 3; background: linear-gradient(90deg, var(--orange-light), var(--orange)); }
  .footer-band .cool { flex: 1; background: linear-gradient(90deg, var(--blue), var(--blue-dark)); display: flex; align-items: center; justify-content: flex-end; padding-right: 8px; }
  .footer-band .cool span { width: 10px; height: 10px; background: var(--paper); display: block; }

  .sheet--fax .wordmark { position: absolute; top: 22px; left: 22px; font-size: 13px; }
  .sheet--fax .mark-square { width: 12px; height: 12px; }
  .fax-title { position: absolute; top: 118px; left: 22px; font-size: 17px; font-weight: 400; letter-spacing: 1px; }
  .fax-fields {
    position: absolute; top: 146px; left: 22px; right: 22px;
    display: grid; grid-template-columns: 1fr 1fr; column-gap: 18px; row-gap: 8px;
    font-size: 5.5px;
  }
  .fax-fields div { border-bottom: 0.8px solid var(--rule); padding-bottom: 2px; }
  .fax-options { position: absolute; top: 236px; left: 22px; right: 22px; display: flex; justify-content: space-between; font-size: 5.5px; }
  .fax-options span::before { content: ""; display: inline-block; width: 6px; height: 6px; border: 0.8px solid var(--ink); margin-right: 3px; vertical-align: -1px; }

  .option-label { position: absolute; top: 508px; font-size: 24px; color: #111; }
  .option-label--one { left: 158px; }
  .option-label--two { left: 520px; }

  /* Envelopes */
  .envelope .flap { position: absolute; top: 0; left: 0; width: 100%; height: 30px; display: block; }
  .envelope .wordmark { position: absolute; font-size: 12px; }
  .envelope .mark-square { width: 11px; height: 11px; }
  .envelope .sender { position: absolute; font-size: 4.5px; line-height: 1.5; }
  .envelope--top { left: 770px; top: 92px; width: 408px; height: 136px; }
  .envelope--top .wordmark { left: 14px; top: 42px; }
  .envelope--top .sender { left: 14px; top: 62px; }
  .envelope--back { left: 876px; top: 238px; width: 300px; height: 146px; }
  .envelope--front { left: 772px; top: 276px; width: 284px; height: 156px; }
  .envelope--front .wordmark { left: 12px; top: 78px; }
  .envelope--front .sender { left: 12px; top: 98px; }

  /* Cards */
  .card { top: 452px; width: 122px; height: 80px; }
  .card--person { left: 772px; }
  .card--brand { left: 924px; top: 456px; }
  .card .wordmark { position: absolute; font-size: 11px; }
  .card .mark-square { width: 9px; height: 9px; }
  .card-text { position: absolute; font-size: 4.3px; line-height: 1.55; white-space: nowrap; }
  .card-text strong { font-weight: 600; font-size: 4.8px; }
  .card--person .card-text { left: 9px; top: 7px; }
  .card--person .wordmark { left: 9px; bottom: 14px; }
  .card--brand .wordmark { left: 8px; top: 30px; }
  .card--brand .card-text { left: 70px; top: 24px; }
  .card-band { position: absolute; left: 0; right: 0; bottom: 0; height: 6px; background: linear-gradient(90deg, var(--orange), var(--orange) 75%, var(--blue) 75%); }
</style>
</head>
<body>

  <!-- Letterhead -->
  <section class="sheet sheet--letter">
    <div class="wordmark"><span class="mark-square"></span>TORV</div>
    <div class="ghost-mark"><span class="ghost-square"></span>TORV</div>
    <footer class="sheet-footer">
      <div class="address">
        <span>Rua das Acácias nº17 Luanda-Angola<br>Tel +244 222 310 417</span>
        <span>marco.telvin@torv-exemplo.com<br>www.torv-exemplo.com</span>
      </div>
      <div class="footer-band"><div class="warm"></div><div class="cool"><span></span></div></div>
    </footer>
  </section>
  <p class="option-label option-label--one">option 1</p>

  <!-- Fax sheet -->
  <section class="sheet sheet--fax">
    <div class="wordmark"><span class="mark-square"></span>TORV</div>
    <h1 class="fax-title">FAX</h1>
    <div class="fax-fields">
      <div>To:</div><div>From:</div>
      <div>Fax:</div><div>Pages:</div>
      <div>Phone:</div><div>Date:</div>
      <div>Re:</div><div>CC:</div>
    </div>
    <div class="fax-options">
      <span>Urgent</span><span>For Review</span><span>Please Comment</span><span>Please Reply</span><span>Please Recycle</span>
    </div>
    <div class="ghost-mark"><span class="ghost-square"></span>TORV</div>
    <footer class="sheet-footer">
      <div class="address">
        <span>Rua das Acácias nº17 Luanda-Angola<br>Tel +244 222 310 417</span>
        <span>www.torv-exemplo.com</span>
      </div>
      <div class="footer-band"><div class="warm"></div><div class="cool"><span></span></div></div>
    </footer>
  </section>
  <p class="option-label option-label--two">option 2</p>

  <!-- Envelopes -->
  <section class="envelope envelope--top">
    <svg class="flap" viewBox="0 0 408 30" preserveAspectRatio="none"><path d="M0 0H408V16H214Q204 28 194 16H0Z" fill="var(--orange)"/></svg>
    <div class="wordmark"><span class="mark-square"></span>TORV</div>
    <p class="sender">Rua das Acácias nº17<br>Luanda-Angola</p>
  </section>

  <section class="envelope envelope--back">
    <svg class="flap" viewBox="0 0 300 30" preserveAspectRatio="none"><path d="M0 0H300V18H160Q150 30 140 18H0Z" fill="var(--grey-flap)"/></svg>
  </section>

  <section class="envelope envelope--front">
    <svg class="flap" viewBox="0 0 284 30" preserveAspectRatio="none"><path d="M0 0H284V14H152Q142 26 132 14H0Z" fill="var(--orange)"/></svg>
    <div class="wordmark"><span class="mark-square"></span>TORV</div>
    <p class="sender">Rua das Acácias nº17<br>Luanda-Angola</p>
  </section>

  <!-- Business cards -->
  <section class="card card--person">
    <p class="card-text"><strong>Marco Daniel Fervone Lusse de Telvin</strong><br>Administrador<br>+244 222 310 417<br>marco.telvin@torv-exemplo.com</p>
    <div class="wordmark"><span class="mark-square"></span>TORV</div>
    <div class="card-band"></div>
  </section>

  <section class="card card--brand">
    <div class="wordmark"><span class="mark-square"></span>TORV</div>
    <p class="card-text">Rua das Acácias nº17<br>Luanda-Angola<br>+244 222 310 417<br>www.torv-exemplo.com</p>
    <div class="card-band"></div>
  </section>

</body>
</html>
```